New business card for my lawn and landscape business

Dorrin Yard and Building is a full-service lawn care, landscaping, and light construction company serving Paragould and the Northeast Arkansas region. The business is owned and operated by Marcus Toller, with a reputation for hands-on, detail-oriented service, dependable crews, and quality results for both residential and commercial clients. A well regarded business with great reviews.
Owner Marcus Toller
Dorrinyardandbuilding.example

Target Market(s)

Commercial, Middle, and upper class in north east Arkansas

Industry/Entity Type

Lawn maintenance and landscape

Contact Information for Business Card

Dorrin Yard And Building Professional lawn care, landscaping, and property improvement in Northeast Arkansas. • lawn maintenance •lawn treatments and weed control • exterior projects • Custom landscape design & installation • Sod, trees, rock & drainage solutions • Residential & commercial services Reliable. Detailed. Done right.

Requirements
Must have
• Business name, service area, list of some of our services, clean design that represents
Nice to have
• Unique. Different design element than just grass because its already in n the logo. Picture of a warm season (south) lawn or landscape. Pictures of the type of work we do

```html
<!DOCTYPE html>
<html lang="en">
<head>
<meta charset="utf-8">
<title>Dorrin Yard &amp; Building – Business Card</title>
<link rel="stylesheet" href="https://fonts.googleapis.com/css2?family=Poppins:wght@400;500;600&display=swap">
<style>
  :root {
    --page: #1b1c1f;
    --card: #25282b;
    --green: #7dbf3b;
    --green-dark: #4f8a22;
    --text: #e4e6e8;
    --muted: #9a9ea3;
    --rule: #6c7075;
  }
  * { margin: 0; padding: 0; box-sizing: border-box; }
  html, body { width: 1200px; height: 800px; overflow: hidden; }
  body {
    background: var(--page);
    font-family: "Poppins", sans-serif;
    color: var(--text);
    position: relative;
  }
  .card {
    position: absolute;
    top: 240px;
    width: 560px;
    height: 320px;
    background: var(--card);
    border-radius: 18px;
    overflow: hidden;
  }
  .card--front { left: 20px; }
  .card--back { left: 620px; }

  .brand {
    position: absolute;
    display: flex;
    align-items: center;
    gap: 12px;
  }
  .brand__dot {
    width: 22px; height: 22px;
    border-radius: 50%;
    background: var(--green);
    flex: none;
  }
  .brand__name {
    font-weight: 600;
    color: var(--green);
    font-size: 24px;
    line-height: 1.1;
    text-transform: uppercase;
    letter-spacing: 1px;
  }
  .card--front .brand { left: 40px; top: 96px; }
  .card--back .brand { right: 40px; top: 50px; }

  .divider {
    position: absolute;
    left: 262px; top: 60px;
    width: 1px; height: 120px;
    background: var(--rule);
  }
  .contact {
    position: absolute;
    left: 284px; top: 54px;
  }
  .contact__name {
    color: var(--green);
    font-weight: 500;
    font-size: 20px;
    letter-spacing: 1px;
    text-transform: uppercase;
  }
  .contact__role { font-size: 11px; color: var(--text); margin-bottom: 10px; }
  .contact__line { font-size: 11px; line-height: 1.55; }
  .contact__row { display: flex; align-items: center; gap: 8px; font-size: 11px; line-height: 1.8; }
  .contact__row svg { width: 11px; height: 11px; fill: var(--green); flex: none; }

  .corner-band, .grass-art { position: absolute; }
  .corner-band { right: 0; top: 0; }
  .grass-art { left: 0; bottom: 0; }

  .services {
    position: absolute;
    left: 40px; bottom: 36px;
  }
  .services__title {
    color: var(--green);
    font-weight: 600;
    font-size: 18px;
    letter-spacing: 1px;
    text-transform: uppercase;
    margin-bottom: 6px;
  }
  .services__list { list-style: none; }
  .services__item {
    display: flex; align-items: center; gap: 10px;
    font-size: 13px; line-height: 1.65;
  }
  .services__item svg { width: 12px; height: 8px; fill: var(--green); flex: none; }
</style>
</head>
<body>

<section class="card card--front">
  <div class="brand">
    <span class="brand__dot"></span>
    <span class="brand__name">Dorrin<br>Yard &amp;<br>Building</span>
  </div>

  <div class="divider"></div>

  <div class="contact">
    <p class="contact__name">Marcus Toller</p>
    <p class="contact__role">CEO</p>
    <p class="contact__line">PO BOX 418 Pine Ridge Road</p>
    <p class="contact__line" style="margin-bottom:6px">Paragould, Arkansas</p>
    <p class="contact__row">
      <svg viewBox="0 0 24 24"><path d="M6.6 10.8a15 15 0 0 0 6.6 6.6l2.2-2.2a1 1 0 0 1 1-.25 11.4 11.4 0 0 0 3.6.57 1 1 0 0 1 1 1V20a1 1 0 0 1-1 1A17 17 0 0 1 3 4a1 1 0 0 1 1-1h3.5a1 1 0 0 1 1 1c0 1.25.2 2.45.57 3.57a1 1 0 0 1-.25 1z"/></svg>
      (870) 555-0142
    </p>
    <p class="contact__row">
      <svg viewBox="0 0 24 24"><path d="M2 5h20v14H2z M2 5l10 8 10-8" /></svg>
      info@dorrinyard.example
    </p>
  </div>

  <svg class="corner-band" width="120" height="150" viewBox="0 0 120 150">
    <polygon points="70,0 120,0 120,150 40,150" fill="var(--green)"/>
  </svg>

  <svg class="grass-art" width="560" height="110" viewBox="0 0 560 110" role="img" aria-label="Green grass blades rising along the bottom edge">
    <defs>
      <linearGradient id="grassTone" x1="0" y1="1" x2="0" y2="0">
        <stop offset="0" stop-color="var(--green)"/>
        <stop offset="1" stop-color="var(--green-dark)" stop-opacity="0.7"/>
      </linearGradient>
    </defs>
    <polygon points="180,110 560,110 560,10 180,90" fill="url(#grassTone)"/>
  </svg>
</section>

<section class="card card--back">
  <div class="brand">
    <span class="brand__dot"></span>
    <span class="brand__name">Dorrin<br>Yard &amp;<br>Building</span>
  </div>

  <div class="services">
    <p class="services__title">Services</p>
    <ul class="services__list">
      <li class="services__item"><svg viewBox="0 0 12 8"><ellipse cx="6" cy="4" rx="6" ry="3.5"/></svg>Lawn maintenance</li>
      <li class="services__item"><svg viewBox="0 0 12 8"><ellipse cx="6" cy="4" rx="6" ry="3.5"/></svg>Lawn treatments and weed control</li>
      <li class="services__item"><svg viewBox="0 0 12 8"><ellipse cx="6" cy="4" rx="6" ry="3.5"/></svg>Exterior projects</li>
      <li class="services__item"><svg viewBox="0 0 12 8"><ellipse cx="6" cy="4" rx="6" ry="3.5"/></svg>Custom landscape design &amp; installation</li>
      <li class="services__item"><svg viewBox="0 0 12 8"><ellipse cx="6" cy="4" rx="6" ry="3.5"/></svg>Sod, trees, rock &amp; drainage solutions</li>
      <li class="services__item"><svg viewBox="0 0 12 8"><ellipse cx="6" cy="4" rx="6" ry="3.5"/></svg>Residential &amp; commercial services</li>
    </ul>
  </div>
</section>

</body>
</html>
```